Indy Film Production Company/Studio

We need a business card designed from an existing logo. We are a digital studio/production company that caters to creating genre entertainment, like Action, Horror, and martial arts. The card along with the logo will be used to Brand the company from letter heads to banners. The design will also be used for postcards and Brochures. It should be professional and masculine.
Updates

Thank you to all the designers who have participated. I'm narrowing down who it will be. Thank you again.

Target Market(s)

Investors, Networks, Producers, and actors

Industry/Entity Type

Film Production

Contact Information for Business Card

Benedict Harlowe
Producer/Writer/Director
www.pelvarmotionworks.com

Requirements
Must have
• Website address, Facebook icon and Twitter icon possibly in the back of the card.
Nice to have
• Logline of Company: Follow The Action.

```html
<!DOCTYPE html>
<html lang="en">
<head>
<meta charset="utf-8">
<title>Pelvar Motion Works – Business Card</title>
<link rel="stylesheet" href="https://fonts.googleapis.com/css2?family=Roboto+Condensed:ital,wght@0,400;0,700;1,400&display=swap">
<style>
  :root {
    --stage: #d9d6d1;
    --card: #f3f2ef;
    --card-edge: #e2e0dc;
    --brand-red: #c8161d;
    --ink: #2a2a2a;
    --ink-soft: #3c3c3c;
    --band-dark: #151515;
  }
  * { margin: 0; padding: 0; box-sizing: border-box; }
  html, body { width: 1200px; height: 969px; overflow: hidden; }
  body {
    background: var(--stage);
    font-family: "Roboto Condensed", "Arial Narrow", sans-serif;
    position: relative;
  }
  .business-card {
    position: absolute;
    left: 100px; top: 201px;
    width: 1000px; height: 567px;
    background: var(--card);
    border: 1px solid var(--card-edge);
    box-shadow: 0 10px 30px rgba(0,0,0,0.12);
    overflow: hidden;
  }
  .brand-name {
    position: absolute;
    left: 0; right: 0; top: 150px;
    text-align: center;
    color: var(--brand-red);
    font-weight: 700;
    font-size: 74px;
    letter-spacing: 2px;
    text-transform: uppercase;
    line-height: 1;
  }
  .person {
    position: absolute;
    right: 513px; top: 372px;
    text-align: right;
    text-transform: uppercase;
  }
  .person-name {
    color: var(--brand-red);
    font-weight: 400;
    font-size: 33px;
    letter-spacing: 0.5px;
    line-height: 1.2;
  }
  .person-role {
    color: var(--ink-soft);
    font-size: 26px;
    letter-spacing: 0.5px;
    margin-top: 6px;
  }
  .divider {
    position: absolute;
    left: 518px; top: 364px;
    width: 2px; height: 112px;
    background: var(--ink);
  }
  .contact-list {
    position: absolute;
    left: 556px; top: 364px;
    list-style: none;
  }
  .contact-item {
    display: flex;
    align-items: center;
    height: 38px;
    color: var(--ink);
    font-style: italic;
    font-size: 26px;
  }
  .contact-icon {
    width: 24px; height: 24px;
    margin-right: 12px;
    fill: var(--brand-red);
    flex: none;
  }
  .bottom-band {
    position: absolute;
    left: 0; bottom: 0;
    width: 1000px; height: 24px;
  }
</style>
</head>
<body>
  <div class="business-card">
    <div class="brand-name">Pelvar Motion Works</div>

    <div class="person">
      <div class="person-name">Benedict Harlowe</div>
      <div class="person-role">Producer/Writer/Director</div>
    </div>

    <div class="divider"></div>

    <ul class="contact-list">
      <li class="contact-item">
        <svg class="contact-icon" viewBox="0 0 24 24" aria-hidden="true">
          <path d="M6.6 10.8a15.1 15.1 0 0 0 6.6 6.6l2.2-2.2c.3-.3.7-.4 1-.2 1.1.4 2.3.6 3.6.6.6 0 1 .4 1 1V20c0 .6-.4 1-1 1A17 17 0 0 1 3 4c0-.6.4-1 1-1h3.5c.6 0 1 .4 1 1 0 1.3.2 2.5.6 3.6.1.3 0 .7-.2 1z"/>
        </svg>
        555 0142 7789
      </li>
      <li class="contact-item">
        <svg class="contact-icon" viewBox="0 0 24 24" aria-hidden="true">
          <path d="M2 5h20v14H2z M2 5l10 7 10-7" fill="var(--brand-red)"/>
          <path d="M2 6l10 7 10-7" fill="none" stroke="var(--card)" stroke-width="1.6"/>
        </svg>
        hello@pelvarmotionworks.com
      </li>
      <li class="contact-item">
        <svg class="contact-icon" viewBox="0 0 24 24" aria-hidden="true">
          <circle cx="12" cy="12" r="10"/>
          <g fill="none" stroke="var(--card)" stroke-width="1.4">
            <ellipse cx="12" cy="12" rx="4" ry="10"/>
            <path d="M2 12h20M4 7h16M4 17h16"/>
          </g>
        </svg>
        www.pelvarmotionworks.com
      </li>
    </ul>

    <svg class="bottom-band" viewBox="0 0 1000 24" preserveAspectRatio="none" aria-hidden="true">
      <defs>
        <linearGradient id="band-red" x1="0" y1="0" x2="0" y2="1">
          <stop offset="0" stop-color="#e0262d"/>
          <stop offset="1" stop-color="#a80f15"/>
        </linearGradient>
      </defs>
      <polygon points="0,4 740,4 760,24 0,24" fill="url(#band-red)"/>
      <polygon points="752,0 1000,0 1000,24 774,24" fill="var(--band-dark)"/>
    </svg>
  </div>
</body>
</html>
```